Showroom Signage Design – Bright Hinges (High-Exposure Road Frontage)

Project Overview
We are looking for a creative designer to develop large-scale external signage for the Bright Hinges showroom.
The building is a double-storey showroom with full glass frontage positioned on a very busy main road.
The glazing spans both levels and we want to utilise the façade like a large billboard that captures attention from passing traffic.
The design must be bold, clean, professional, and highly readable at speed.
About Bright Hinges:
Bright Hinges specialises in cabinetry face-lifts / renovations.
including:
Our Core Service — Cabinetry Facelifts
- Kitchens
- Bathrooms
- Laundries
- Wardrobes
We Also Offer New Installations:
- Kitchens
- Bathrooms
- Laundries
- Wardrobes
We want the signage to clearly communicate that we are experts in facelifting / renovating spaces, while also providing complete new cabinetry solutions.
We will remove the reflective film on the windows for the lower level. There will be a kitchen showing in the middle of the lower level. So we don't want signage infront of the kitchen area. (Attached is a screenshot of the office with blue and pink squares. The blue is the location of the kitchen internally, and the pink can be signage design spaces.) Ideally the printing wont have a solid colour background for printing on the lower level.
Design Goals:
- Turns the entire glazed frontage into a visual billboard
- Works across two storeys
- Is highly visible from passing vehicles
- Uses strong hierarchy and minimal clutter
- Clearly communicates our services at a glance
- Encourages customers to visit the showroom
Think impact first, then detail.
Key Considerations
- Viewed primarily by drive-by traffic
- Must read clearly from distance and speed
- Should utilise window graphics, scale, and layout effectively
- Design should enhance — not block — natural light where possible
- Must feel architectural and professional, not retail clutter
Deliverables:
Print-ready vector files (AI/EPS/PDF)
Building mockups showing real-world application
We are looking for a design that makes Bright Hinges impossible to miss — transforming the showroom frontage into a powerful advertising statement.
Target Market(s)
Renovation clients on a budget, but also clients wanting an efficient turn around of high end projects.
Colors
Designer to choose only greyscale colors for use in the design.
Look and feel

```html
<!DOCTYPE html>
<html lang="en">
<head>
<meta charset="utf-8">
<title>Bright Hinges Kitchens – Showroom Frontage Signage</title>
<link href="https://fonts.googleapis.com/css2?family=Montserrat:ital,wght@0,400;0,600;0,800;0,900;1,800;1,900&display=swap" rel="stylesheet">
<style>
  :root {
    --ink: #3a3a3c;
    --paper: #f3f3f3;
    --paper-mid: #e6e6e6;
    --stage: #d9dadb;
  }
  * { box-sizing: border-box; margin: 0; padding: 0; }
  html, body { width: 1200px; height: 781px; overflow: hidden; }
  body {
    background: var(--stage);
    font-family: "Montserrat", Arial, sans-serif;
    color: var(--ink);
    position: relative;
  }
  .frontage { position: absolute; inset: 0; }

  /* upper storey billboard */
  .billboard {
    position: absolute; left: 75px; top: 70px; width: 685px; height: 370px;
    background: var(--paper);
  }
  .billboard-shapes { position: absolute; inset: 0; }
  .brand {
    position: absolute; left: 120px; top: 70px; width: 400px;
    display: flex; align-items: center; justify-content: center; gap: 10px;
  }
  .brand-square { width: 14px; height: 14px; background: var(--ink); flex: none; }
  .brand-name { font-weight: 900; font-size: 23px; letter-spacing: -0.3px; line-height: 1; white-space: nowrap; }
  .brand-tag {
    position: absolute; left: 145px; top: 98px; width: 345px;
    font-weight: 600; font-size: 10.5px; letter-spacing: 0.6px; text-align: center;
    display: flex; align-items: center; gap: 8px; white-space: nowrap;
  }
  .brand-tag::before, .brand-tag::after { content: ""; flex: 1; height: 2px; background: var(--ink); }
  .offer-box {
    position: absolute; left: 140px; top: 140px; width: 352px; height: 31px;
    border: 2px solid var(--ink);
    font-style: italic; font-weight: 800; font-size: 14px;
    display: flex; align-items: center; justify-content: center; white-space: nowrap;
  }
  .headline { position: absolute; left: 60px; top: 172px; width: 520px; text-align: center; line-height: 0.92; }
  .headline .line { display: block; white-space: nowrap; }
  .headline .small { font-weight: 800; font-size: 30px; }
  .headline .big { font-weight: 900; font-size: 56px; letter-spacing: -1.5px; }
  .specialty {
    position: absolute; left: 94px; top: 278px; width: 437px; height: 30px;
    background: var(--ink); color: var(--paper);
    font-style: italic; font-weight: 800; font-size: 13.5px;
    display: flex; align-items: center; justify-content: center; white-space: nowrap;
  }
  .icon-rail {
    position: absolute; left: 622px; top: 73px; width: 50px; height: 294px;
    display: flex; flex-direction: column; justify-content: space-between; align-items: center;
  }
  .icon-disc { width: 50px; height: 50px; border-radius: 50%; background: var(--ink); display: flex; align-items: center; justify-content: center; }
  .icon-disc svg { width: 28px; height: 28px; }

  /* right upper panel */
  .name-panel {
    position: absolute; left: 798px; top: 195px; width: 160px; height: 155px;
    background: var(--paper);
    display: flex; align-items: center; justify-content: center;
  }
  .name-panel .panel-name {
    font-weight: 900; font-size: 26px; line-height: 1.05; text-align: center; letter-spacing: -0.5px;
  }
  .slogan {
    position: absolute; left: 758px; top: 390px; width: 205px; height: 52px;
    background: var(--paper);
    clip-path: polygon(15% 0, 100% 0, 100% 100%, 0 100%);
    text-align: center; padding-top: 9px; padding-left: 14px; line-height: 1.05;
  }
  .slogan .top { font-weight: 400; font-size: 14px; letter-spacing: 0.5px; display: block; white-space: nowrap; }
  .slogan .bottom { font-weight: 800; font-size: 14px; display: block; white-space: nowrap; }
  .slogan .tag { background: var(--ink); color: var(--paper); padding: 0 4px; }

  /* lower storey service panels */
  .service-panel {
    position: absolute; top: 440px; width: 166px; height: 195px;
    display: flex; flex-direction: column;
  }
  .service-panel.left { left: 66px; }
  .service-panel.right { left: 588px; width: 170px; }
  .service-half {
    flex: 1; display: flex; flex-direction: column; align-items: center; justify-content: center; gap: 6px;
  }
  .service-half.dark { background: var(--ink); color: var(--paper); }
  .service-half.light { background: var(--paper); color: var(--ink); }
  .service-icon { width: 32px; height: 32px; }
  .service-name { font-style: italic; font-weight: 800; font-size: 10.5px; letter-spacing: 0.2px; }
  .service-label {
    position: absolute; left: 50%; top: 50%; transform: translate(-50%, -50%);
    background: var(--paper); border: 2px solid var(--ink);
    font-weight: 900; font-size: 14px; padding: 2px 8px; border-radius: 2px;
  }
  .kitchen-view {
    position: absolute; left: 232px; top: 440px; width: 356px; height: 192px;
    background: linear-gradient(180deg, #8c9294 0%, #a7a9a6 55%, #8e8a82 100%);
    opacity: 0.55;
  }
</style>
</head>
<body>
<main class="frontage">

  <section class="billboard">
    <svg class="billboard-shapes" viewBox="0 0 685 370" width="685" height="370" aria-hidden="true">
      <polygon points="210,30 605,8 605,35 440,30" fill="#3a3a3c"/>
      <rect x="605" y="0" width="80" height="370" fill="#e6e6e6"/>
      <rect x="0" y="345" width="605" height="25" fill="#e6e6e6"/>
      <polygon points="0,345 0,370 150,370" fill="#3a3a3c"/>
    </svg>

    <div class="brand"><span class="brand-square"></span><span class="brand-name">BRIGHT HINGES KITCHENS</span></div>
    <div class="brand-tag">FRESH CABINET MAKEOVERS</div>
    <div class="offer-box">EXPERT FACELIFTS &amp; NEW INSTALLATIONS</div>
    <h1 class="headline">
      <span class="line"><span class="small">DON’T </span><span class="big">SCRAP</span><span class="small"> IT.</span></span>
      <span class="line"><span class="big">REVIVE</span><span class="small"> IT.</span></span>
    </h1>
    <div class="specialty">SPECIALISES IN CABINETRY FACELIFTS / RENOVATIONS</div>

    <div class="icon-rail">
      <div class="icon-disc"><svg viewBox="0 0 28 28" fill="#f3f3f3" role="img" aria-label="Bathrooms"><rect x="4" y="13" width="20" height="8"/><rect x="12" y="7" width="4" height="6"/><rect x="6" y="21" width="3" height="3"/><rect x="19" y="21" width="3" height="3"/></svg></div>
      <div class="icon-disc"><svg viewBox="0 0 28 28" fill="#f3f3f3" role="img" aria-label="Laundries"><rect x="3" y="12" width="11" height="12"/><rect x="15" y="5" width="10" height="19"/><circle cx="8.5" cy="18" r="3" fill="#3a3a3c"/></svg></div>
      <div class="icon-disc"><svg viewBox="0 0 28 28" fill="#f3f3f3" role="img" aria-label="Kitchens"><rect x="3" y="14" width="22" height="10"/><rect x="15" y="4" width="10" height="7"/><polygon points="5,11 9,5 13,11"/></svg></div>
      <div class="icon-disc"><svg viewBox="0 0 28 28" fill="#f3f3f3" role="img" aria-label="Wardrobes"><rect x="4" y="4" width="20" height="18"/><rect x="13.5" y="4" width="1" height="18" fill="#3a3a3c"/><rect x="5" y="22" width="3" height="3"/><rect x="20" y="22" width="3" height="3"/></svg></div>
    </div>
  </section>

  <section class="name-panel"><span class="panel-name">BRIGHT<br>HINGES</span></section>

  <p class="slogan"><span class="top">MAKE YOUR ROOM</span><span class="bottom">FEEL <span class="tag">BRAND NEW</span></span></p>

  <section class="service-panel left">
    <div class="service-half dark">
      <svg class="service-icon" viewBox="0 0 28 28" fill="none" stroke="#f3f3f3" stroke-width="2"><circle cx="14" cy="14" r="13"/><rect x="7" y="14" width="14" height="7"/><rect x="15" y="8" width="6" height="4"/></svg>
      <span class="service-name">KITCHENS</span>
    </div>
    <div class="service-half light">
      <svg class="service-icon" viewBox="0 0 28 28" fill="none" stroke="#3a3a3c" stroke-width="2"><circle cx="14" cy="14" r="13"/><rect x="7" y="13" width="14" height="6"/><rect x="12.5" y="8" width="3" height="5"/></svg>
      <span class="service-name">BATHROOMS</span>
    </div>
    <span class="service-label">SERVICE</span>
  </section>

  <div class="kitchen-view" role="img" aria-label="Clear glazing showing the showroom kitchen display behind"></div>

  <section class="service-panel right">
    <div class="service-half light">
      <svg class="service-icon" viewBox="0 0 28 28" fill="none" stroke="#3a3a3c" stroke-width="2"><circle cx="14" cy="14" r="13"/><rect x="7" y="12" width="7" height="8"/><rect x="15" y="8" width="6" height="12"/></svg>
      <span class="service-name">LAUNDRIES</span>
    </div>
    <div class="service-half dark">
      <svg class="service-icon" viewBox="0 0 28 28" fill="none" stroke="#f3f3f3" stroke-width="2"><circle cx="14" cy="14" r="13"/><rect x="8" y="8" width="12" height="12"/><line x1="14" y1="8" x2="14" y2="20"/></svg>
      <span class="service-name">WARDROBES</span>
    </div>
    <span class="service-label">SERVICE</span>
  </section>

</main>
</body>
</html>
```